Beauty Clinic Treatment Menu (Lumen Nails & Beauty)

Needing a treatment menu designed for a beauty clinic in Kaiwhero, New Zealand. Like the colours grey, pink, white.
Elegant, Modern and feminine

Lumen Nails & Beauty
Karen Pell
Room3, 48 Tainui Street
Kaiwhero
0273816240
Karen.lumen@mailbox.test
lumenbeauty.co.nz

Target Market(s)

Females

Industry/Entity Type

Beauty Salon

Font styles to use
Serif

Colors

Requirements
Must have
• Chatterly and Snapgrid logo

```html
<!DOCTYPE html>
<html lang="en">
<head>
<meta charset="utf-8">
<title>Lumen Nails &amp; Beauty – Treatment Menu</title>
<link rel="stylesheet" href="https://fonts.googleapis.com/css2?family=EB+Garamond:wght@400;500&family=Playfair+Display:wght@700&display=swap">
<style>
  :root {
    --pink-deep: #d63d7d;
    --pink-head: #e8739f;
    --pink-band: #ee7fb0;
    --pink-soft: #fbe6f0;
    --brown-text: #6b4a3a;
    --grey-dark: #555555;
    --grey-mid: #a9a9a9;
    --white: #ffffff;
    --serif: "EB Garamond", Georgia, serif;
    --display: "Playfair Display", Georgia, serif;
  }
  html, body { margin: 0; padding: 0; overflow: hidden; background: var(--white); }
  .canvas { position: relative; width: 824px; height: 1200px; overflow: hidden; background: var(--white); }
  .sheet { position: absolute; display: block; }
  .sheet--outside { left: 22px; top: 30px; width: 774px; height: 561px; }
  .sheet--inside { left: 16px; top: 609px; width: 791px; height: 574px; }
  .display { font-family: var(--display); }
  .contact { font-family: var(--serif); font-size: 39px; fill: var(--brown-text); text-anchor: middle; }
  .contact--accent { fill: var(--pink-deep); font-size: 52px; }
  .brand-name { font-family: var(--serif); font-weight: 400; fill: var(--brown-text); text-anchor: middle; }
  .cover-title { font-family: var(--serif); font-weight: 500; fill: var(--pink-deep); text-anchor: end; }
  .section-title { font-family: var(--serif); fill: var(--white); font-size: 50px; letter-spacing: 1px; }
  .group-title { font-family: var(--serif); fill: var(--pink-head); font-size: 33px; letter-spacing: 1px; }
  .item { font-family: var(--serif); fill: var(--grey-dark); font-size: 28px; }
  .note { font-family: var(--serif); fill: var(--grey-dark); font-size: 15px; text-anchor: middle; }
  .facial-title { font-family: var(--serif); fill: var(--grey-dark); font-size: 28px; text-anchor: middle; }
  .facial-note { font-family: var(--serif); fill: var(--grey-dark); font-size: 16px; text-anchor: middle; }
</style>
</head>
<body>
<div class="canvas">

  <!-- Outside of the tri-fold -->
  <svg class="sheet sheet--outside" viewBox="40 55 1410 1022" xmlns="http://www.w3.org/2000/svg">
    <defs>
      <linearGradient id="leftPanelFill" x1="0" y1="0" x2="0" y2="1">
        <stop offset="0" stop-color="#fde9f3"/>
        <stop offset="0.5" stop-color="#f6f2f4"/>
        <stop offset="1" stop-color="#c6c6c6"/>
      </linearGradient>
      <linearGradient id="facialPhotoFill" x1="0" y1="0" x2="1" y2="1">
        <stop offset="0" stop-color="#d9d9d9"/>
        <stop offset="0.45" stop-color="#e6c3ad"/>
        <stop offset="1" stop-color="#d9a892"/>
      </linearGradient>
      <linearGradient id="handPhotoFill" x1="0" y1="0" x2="1" y2="1">
        <stop offset="0" stop-color="#f3d4c4"/>
        <stop offset="1" stop-color="#e9b9a3"/>
      </linearGradient>
      <linearGradient id="swooshGrey" x1="0" y1="0" x2="0" y2="1">
        <stop offset="0" stop-color="#ffffff"/>
        <stop offset="1" stop-color="#bdbdbd"/>
      </linearGradient>
      <radialGradient id="petalFill">
        <stop offset="0" stop-color="#e27ad1"/>
        <stop offset="1" stop-color="#f2b5e4" stop-opacity="0"/>
      </radialGradient>
    </defs>

    <rect x="40" y="55" width="435" height="1022" fill="url(#leftPanelFill)"/>
    <rect x="475" y="55" width="445" height="1022" fill="#efdde6"/>
    <rect x="920" y="55" width="530" height="1022" fill="var(--pink-soft)"/>

    <rect x="478" y="290" width="972" height="787" fill="url(#facialPhotoFill)" role="img" aria-label="Photo of a client receiving a facial treatment with a handheld device"/>

    <path d="M475,300 C650,250 810,300 905,470 C960,560 1100,610 1250,560 C1350,520 1420,420 1450,380 L1450,520 C1300,620 1120,650 990,615 C850,575 800,440 650,405 C560,385 500,395 475,410 Z" fill="url(#swooshGrey)"/>
    <path d="M475,300 C650,250 810,300 905,470 C960,545 1100,585 1250,540 C1350,505 1420,420 1450,380 L1450,470 C1330,560 1150,600 1010,570 C880,540 800,420 650,380 C560,360 500,370 475,380 Z" fill="var(--white)"/>

    <path d="M40,460 C200,380 380,300 560,330 C700,352 820,470 960,565 C820,530 700,425 560,395 C400,365 220,470 40,565 Z" fill="var(--pink-band)"/>

    <rect x="120" y="130" width="310" height="200" rx="30" fill="url(#handPhotoFill)" role="img" aria-label="Photo of a hand with blue manicured nails"/>
    <ellipse cx="280" cy="415" rx="60" ry="58" fill="url(#petalFill)" role="img" aria-label="Scattered pink rose petals"/>
    <ellipse cx="1400" cy="350" rx="45" ry="45" fill="url(#petalFill)" role="img" aria-label="Pink rose petals"/>

    <!-- small brand name -->
    <text class="brand-name" x="707" y="353" font-size="30">Lumen</text>

    <!-- brand name on plain circle -->
    <circle cx="1160" cy="465" r="102" fill="var(--white)"/>
    <text class="brand-name" x="1160" y="483" font-size="56">Lumen</text>

    <!-- title -->
    <text class="cover-title" x="1395" y="195" font-size="84" textLength="440" lengthAdjust="spacingAndGlyphs">LUMEN NAILS</text>
    <text class="cover-title" x="1395" y="285" font-size="96" textLength="420" lengthAdjust="spacingAndGlyphs">&amp; BEAUTY</text>

    <!-- contact -->
    <text class="contact" x="262" y="625">Lumen Nails &amp; Beauty</text>
    <text class="contact contact--accent" x="252" y="678">Karen Pell</text>
    <text class="contact" x="257" y="726">Room3, 48 Tainui Street</text>
    <text class="contact" x="250" y="773">Kaiwhero</text>
    <text class="contact contact--accent" x="252" y="826">0273816240</text>
    <text class="contact" x="272" y="863">Karen.lumen@mailbox.test</text>
    <text class="contact" x="273" y="904">lumenbeauty.co.nz</text>
  </svg>

  <!-- Inside of the tri-fold: treatment menu -->
  <svg class="sheet sheet--inside" viewBox="30 1110 1440 1045" xmlns="http://www.w3.org/2000/svg">
    <defs>
      <linearGradient id="menuPink" x1="0" y1="0" x2="0" y2="1">
        <stop offset="0" stop-color="#f4aecb"/>
        <stop offset="1" stop-color="#fbd3e4"/>
      </linearGradient>
      <linearGradient id="menuGrey" x1="0" y1="0" x2="1" y2="1">
        <stop offset="0" stop-color="#8f8f8f"/>
        <stop offset="1" stop-color="#d4d4d4"/>
      </linearGradient>
      <linearGradient id="menuWhite" x1="0" y1="0" x2="0" y2="1">
        <stop offset="0" stop-color="#ffffff"/>
        <stop offset="1" stop-color="#e4e4e4"/>
      </linearGradient>
      <radialGradient id="menuPetal">
        <stop offset="0" stop-color="#e36cb0"/>
        <stop offset="1" stop-color="#f4a9cf" stop-opacity="0"/>
      </radialGradient>
    </defs>

    <rect x="30" y="1110" width="1440" height="1045" fill="url(#menuPink)"/>
    <rect x="560" y="1110" width="455" height="1045" fill="#e7a9c4" opacity="0.35"/>

    <path d="M30,1440 C250,1340 480,1380 620,1520 C760,1660 900,1700 1050,1640 C1250,1560 1380,1400 1470,1310 L1470,2155 L30,2155 Z" fill="url(#menuGrey)"/>
    <path d="M30,1595 C220,1450 430,1420 600,1560 C720,1660 850,1720 1000,1690 C1150,1660 1300,1500 1470,1380 L1470,1410 C1300,1560 1160,1720 1060,1760 L1060,2155 L30,2155 Z" fill="url(#menuWhite)"/>
    <path d="M660,1682 C800,1760 1000,1725 1200,1600 C1320,1522 1420,1435 1470,1398 L1470,1445 C1380,1505 1280,1585 1180,1652 C1000,1770 820,1775 660,1690 Z" fill="var(--pink-band)"/>
    <path d="M1042,1690 C1065,1850 960,2050 820,2155" fill="none" stroke="var(--grey-mid)" stroke-width="4"/>

    <ellipse cx="75" cy="1185" rx="48" ry="60" fill="url(#menuPetal)" role="img" aria-label="Pink rose petals"/>

    <text class="display" x="787" y="1245" font-size="86" font-weight="700" fill="var(--pink-deep)" text-anchor="middle" textLength="205" lengthAdjust="spacingAndGlyphs">MENU</text>

    <!-- nails -->
    <text class="section-title" x="348" y="1322" text-anchor="middle">NAILS</text>
    <text class="group-title" x="268" y="1490">MANICURE</text>
    <text class="item" x="268" y="1528">Gel Polish - $45</text>
    <text class="item" x="268" y="1565">Regular Pjlish - $40</text>
    <text class="group-title" x="158" y="1618">REDICURE</text>
    <text class="item" x="158" y="1655">Gel Polish - $45</text>
    <text class="item" x="158" y="1692">Regular Pjlish - $40</text>
    <text class="group-title" x="290" y="1757" text-anchor="middle">LUXURY REDICURE</text>
    <text class="note" x="295" y="1785">Includes : soak, exfoliation, heel rasping and massage.</text>
    <text class="item" x="185" y="1815">Gel Polish - $60</text>
    <text class="item" x="185" y="1852">Regular Pjlish - $55</text>
    <text class="group-title" x="305" y="1918" text-anchor="middle">GEL REMOVAL &amp; NALL TIDY-25$</text>
    <text class="group-title" x="284" y="1953" text-anchor="middle">ADD ON</text>
    <text class="item" x="182" y="1988">Gel Removal - $5</text>
    <text class="item" x="182" y="2023">NBX - $5 per layer</text>
    <text class="item" x="182" y="2058">Builder Gel - $10</text>
    <text class="item" x="182" y="2092">Nail Art / Glitter - $POA</text>

    <!-- facials -->
    <text class="section-title" x="795" y="1322" text-anchor="middle">FACIALS</text>
    <text class="facial-title" x="795" y="1407">Deep Cleasing Facial - $75</text>
    <text class="note" x="790" y="1435">45 minutes</text>
    <text class="facial-note" x="795" y="1460">Removes build up of dead skin cell, leaves the ckin feeling</text>
    <text class="facial-note" x="787" y="1480">soft and hydrated.</text>
    <text class="facial-title" x="792" y="1562">Therapeutic Facial - $105</text>
    <text class="note" x="795" y="1588">60 minutes</text>
    <text class="facial-note" x="793" y="1608">Tailored to suit your skins specific needs.</text>
    <text class="facial-title" x="798" y="1745">Rejuvenaition Facial - $120</text>
    <text class="note" x="790" y="1770">60 minutes</text>
    <text class="facial-note" x="795" y="1792">Active yet gentle treatment that facilitaes dermal</text>
    <text class="facial-note" x="787" y="1813">rejuvenation.</text>
    <text class="facial-title" x="793" y="1873">35% Glycolic Facial - $120</text>
    <text class="note" x="790" y="1901">60 minutes</text>
    <text class="facial-note" x="798" y="1926">Hydrating, deep exfoliation treatment improving skin</text>
    <text class="facial-note" x="802" y="1947">texture and appearance.</text>
    <text class="facial-title" x="765" y="2010">Dermaplaning - $120</text>
    <text class="facial-note" x="760" y="2040">Creates a smooth and radiant skin surface.</text>
    <text class="facial-note" x="767" y="2060">Also removes soft facial hairs.</text>

    <!-- eyes -->
    <text class="section-title" x="1120" y="1327">EYES</text>
    <text class="item" x="1118" y="1359">Yori Lash Lift - $115</text>
    <text class="item" x="1118" y="1388">Eyebrow Shape - $19</text>
    <text class="item" x="1118" y="1416">Eyebrow Tint - $18</text>
    <text class="item" x="1118" y="1444">Eyelash Tint - $25</text>
    <text class="item" x="1118" y="1472">Eye Ttio - $45</text>

    <!-- face -->
    <text class="section-title" x="1268" y="1587">FACE</text>
    <text class="item" x="1265" y="1628">Lip - $15</text>
    <text class="item" x="1265" y="1663">Chin - $15</text>

    <!-- body -->
    <text class="section-title" x="1112" y="1762">BODY</text>
    <text class="item" x="1116" y="1800">Under Arm - $20</text>
    <text class="item" x="1116" y="1835">1/2 Leg - $35</text>
    <text class="item" x="1116" y="1870">Full Leg - $55</text>
    <text class="item" x="1116" y="1906">1/2 Arm - $30</text>
    <text class="item" x="1116" y="1941">Full Arm - $40</text>
    <text class="item" x="1116" y="1976">Bikini - $28</text>
    <text class="item" x="1116" y="2011">Extended Bikini - $38</text>
    <text class="item" x="1116" y="2046">Brazilian (1st Time) - $65</text>
    <text class="item" x="1116" y="2080">Brazilian (4-6 Weeks) - $50</text>
    <text class="item" x="1116" y="2107">Patches - $5</text>
  </svg>

</div>
</body>
</html>
```